Liposomal Powders and Excipient Free Manufacturing

I’m seeking a talented designer to refine and elevate a PowerPoint presentation aimed at healthcare professionals. The goal is to ensure the slides are clean, professional, and visually aligned with a scientific audience while remaining engaging and easy to follow.
What I Need:
- Optimisation of slide layouts for clarity and visual impact.
- Creation of a cohesive master template that reflects the brand’s professional and scientific tone.
- Use of brand guidelines (including fonts, colours, and logos) to maintain consistency.
- Strategic incorporation of relevant images, graphics, or icons to make the content more engaging and support the messaging.
- A final design that feels polished, modern, and ready for professional delivery.
What I’ll Provide:
- Current PowerPoint presentation.
- Brand guidelines with fonts, colours, and logo files.

Ideal Designer:
- Experienced in professional or corporate PowerPoint design.
- Comfortable working with scientific or healthcare-related content.
- Able to deliver a clean, visually cohesive presentation that feels on-brand and audience-appropriate.

```html
<!DOCTYPE html>
<html lang="en">
<head>
<meta charset="utf-8">
<title>Smarter Delivery – Slide Overview</title>
<link href="https://fonts.googleapis.com/css2?family=Lato:wght@400;700;900&display=swap" rel="stylesheet">
<style>
:root{
  --stage:#646464;
  --teal:#159eb0;
  --teal-soft:#5cc4d1;
  --card:#e7f8fa;
  --ink:#1b1b1b;
  --muted:#2d2d2d;
  --white:#ffffff;
  --band:#262626;
}
*{box-sizing:border-box;margin:0;padding:0}
html,body{width:1039px;height:1200px;overflow:hidden;background:var(--stage);font-family:'Lato',sans-serif;color:var(--ink)}
.canvas{position:relative;width:1039px;height:1200px}
.slide{position:absolute;width:443px;height:249px;background:var(--white);overflow:hidden}
.col-a{left:63px}.col-b{left:528px}
.row-1{top:69px}.row-2{top:342px}.row-3{top:613px}.row-4{top:885px}

.brand{position:absolute;display:flex;align-items:center;gap:4px;font-weight:400;color:#3a3a3a;letter-spacing:.2px}
.brand-dot{width:15px;height:15px;border-radius:50%;background:var(--teal)}
.brand-name{font-size:10px}

.header-brand{left:10px;top:14px}
.header-rule{position:absolute;left:117px;top:0;width:1px;height:35px;background:#bfbfbf}
.header-title{position:absolute;left:132px;top:13px;font-size:11.5px;font-weight:900;letter-spacing:-.1px}
.corner-dots{position:absolute;right:0;top:0;width:52px;height:48px;background:radial-gradient(circle at 100% 0,rgba(92,196,209,.15),rgba(92,196,209,.6) 40%,rgba(92,196,209,.2) 70%,transparent 72%)}

.bullets{list-style:none}
.bullets li{position:relative;padding-left:12px}
.bullets li::before{content:"";position:absolute;left:0;width:4px;height:4px;border-radius:50%;background:var(--teal)}

/* Title slide */
.title-brand{left:23px;top:20px}
.title-brand .brand-dot{width:22px;height:22px}
.title-brand .brand-name{font-size:13px}
.title-main{position:absolute;left:23px;top:80px;font-size:19px;font-weight:900;color:var(--teal)}
.title-sub{position:absolute;left:23px;top:116px;font-size:14px;line-height:18.3px}
.title-sub strong{font-weight:700}
.title-sub .accent{color:var(--teal);font-weight:700}
.title-band{position:absolute;left:0;top:211px;width:211px;height:18px;background:var(--band);clip-path:polygon(0 0,100% 0,97% 100%,0 100%);color:#f2f2f2;font-size:8.2px;padding:4px 0 0 23px}
.title-burst{position:absolute;left:224px;top:0;width:219px;height:249px;background:radial-gradient(circle at 60% 50%,rgba(21,158,176,.15) 0,rgba(21,158,176,.55) 35%,rgba(21,158,176,.85) 55%,rgba(255,255,255,0) 72%)}

/* Agenda */
.agenda-card{position:absolute;top:55px;width:203px;height:180px;background:var(--card);border-radius:6px;padding:15px 14px}
.agenda-card.first{left:14px}.agenda-card.second{left:226px}
.pill{display:inline-block;background:var(--teal);color:var(--white);font-size:6.5px;font-weight:900;padding:2px 6px;border-radius:8px}
.agenda-card h3{font-size:10.5px;font-weight:700;margin:6px 0 10px;line-height:13px}
.agenda-card .bullets li{font-size:6.6px;line-height:11px;margin-bottom:7.5px}
.agenda-card .bullets li::before{top:4px}

/* Section */
.section-top{position:absolute;left:0;top:0;width:443px;height:64px;background:linear-gradient(90deg,#eef1f3,#f6f7f8 50%,#dfe4e8)}
.section-brand{left:171px;top:20px}
.section-band{position:absolute;left:0;top:64px;width:443px;height:137px;background:var(--teal);color:var(--white);text-align:center;font-weight:900}
.section-band .part{font-size:19px;margin-top:26px}
.section-band .name{font-size:20px;line-height:26px;margin-top:12px}
.section-bottom{position:absolute;left:0;top:201px;width:443px;height:48px;background:linear-gradient(90deg,#f1f3f5,#e3e7ea)}

/* Why */
.why-photo{position:absolute;left:0;top:45px;width:266px;height:204px;background:linear-gradient(135deg,#6f9fb6,#cfe1ea 45%,#8fb2c4)}
.why-panel{position:absolute;left:209px;top:58px;width:234px;height:129px;background:var(--white);padding:13px 12px}
.why-block h4{font-size:9px;font-weight:900;display:flex;align-items:center;gap:6px}
.why-block p{font-size:6.5px;line-height:10.5px;margin-top:4px}
.why-block + .why-block{margin-top:20px}
.icon{width:12px;height:12px}
.why-punch{position:absolute;left:286px;top:200px;font-size:13px;line-height:18.5px}

/* Liposome */
.lipo-figure{position:absolute;left:20px;top:58px;width:189px;height:162px;background:radial-gradient(ellipse at 45% 55%,#3fb7a8,#1f8f8f 50%,rgba(255,255,255,0) 72%)}
.lipo-rule{position:absolute;left:245px;top:66px;width:3px;height:147px;background:var(--teal)}
.lipo-text{position:absolute;left:271px;top:68px;width:160px;font-size:13px;line-height:17.4px}

/* Stability */
.stab-list{position:absolute;left:14px;top:72px}
.stab-list li{font-size:11.3px;line-height:14px;margin-bottom:16px}
.stab-list li::before{top:5px}
.stab-figure{position:absolute;left:203px;top:52px;width:185px;height:168px;background:radial-gradient(ellipse at 50% 50%,#6fd07a 0,#8a8a2e 35%,#2f5fc4 55%,rgba(255,255,255,0) 70%)}

/* Mechanisms */
.mech-photo{position:absolute;left:0;top:46px;width:170px;height:203px;background:radial-gradient(circle at 45% 65%,#d9a040,#3a7fa8 45%,#1b3f6b)}
.mech-list{position:absolute;left:192px;top:68px;width:240px}
.mech-list li{font-size:11px;line-height:18.5px;margin-bottom:14px}
.mech-list li::before{top:7px}

/* Closing */
.closing{background:var(--teal)}
.closing-dots{position:absolute;left:0;top:0;width:200px;height:249px;background:radial-gradient(circle at 100% 50%,rgba(255,255,255,.12),rgba(255,255,255,.04) 60%,transparent 75%)}
.closing-brand{left:137px;top:62px;color:var(--white)}
.closing-brand .brand-dot{width:26px;height:26px;background:var(--white)}
.closing-brand .brand-name{font-size:16px}
.closing-title{position:absolute;left:0;width:443px;top:132px;text-align:center;color:var(--white);font-size:40px;font-weight:400}
</style>
</head>
<body>
<main class="canvas">

  <section class="slide col-a row-1">
    <div class="brand title-brand"><span class="brand-dot"></span><span class="brand-name">NUTRIVERA</span></div>
    <h1 class="title-main">SMARTER DELIVERY</h1>
    <p class="title-sub">The Clinical Edge of<br><strong>Novel Liposomal</strong><br><span class="accent">Powders &amp; Excipient-Free</span><br><strong>Manufacturing</strong></p>
    <div class="title-band">Vantra Expo 2025 | Presented by Dr Owen Hartley</div>
    <div class="title-burst" role="img" aria-label="Radiating teal dot pattern"></div>
  </section>

  <section class="slide col-b row-1">
    <div class="brand header-brand"><span class="brand-dot"></span><span class="brand-name">NUTRIVERA</span></div>
    <div class="header-rule"></div>
    <h2 class="header-title">AGENDA</h2>
    <div class="corner-dots" role="img" aria-label="Teal dot pattern"></div>
    <div class="agenda-card first">
      <span class="pill">PART I</span>
      <h3>Liposomal Innovation &amp;<br>Super-Dried Powders</h3>
      <ul class="bullets">
        <li>Why Delivery Technology Matters</li>
        <li>Liposome Basics → Powders → Stability</li>
        <li>Clinical Evidence (Vitamin B12, Vitamin C, CoQ10, Iron, PEA, Glutathione, Resveratrol)</li>
        <li>Manufacturing Essentials: Spray &amp; Lyophilization Drying, Stability Considerations</li>
      </ul>
    </div>
    <div class="agenda-card second">
      <span class="pill">PART 2</span>
      <h3>Clean Manufacturing</h3>
      <ul class="bullets">
        <li>Excipient-Free Manufacturing: Why It Matters</li>
        <li>Case Studies &amp; Challenges</li>
        <li>Key Takeaways</li>
        <li>Q&amp;A</li>
      </ul>
    </div>
  </section>

  <section class="slide col-a row-2">
    <div class="section-top" role="img" aria-label="Photo of a scientist in a laboratory"></div>
    <div class="brand section-brand"><span class="brand-dot"></span><span class="brand-name">NUTRIVERA</span></div>
    <div class="section-band">
      <p class="part">PART I</p>
      <p class="name">LIPOSOMAL INNOVATION &amp;<br>SUPER-DRIED POWDERS</p>
    </div>
    <div class="section-bottom" role="img" aria-label="Blurred laboratory photo"></div>
  </section>

  <section class="slide col-b row-2">
    <div class="brand header-brand"><span class="brand-dot"></span><span class="brand-name">NUTRIVERA</span></div>
    <div class="header-rule"></div>
    <h2 class="header-title">WHY DELIVERY TECHNOLOGY MATTERS?</h2>
    <div class="corner-dots" role="img" aria-label="Teal dot pattern"></div>
    <div class="why-photo" role="img" aria-label="Photo of a researcher taking notes beside a microscope"></div>
    <div class="why-panel">
      <div class="why-block">
        <h4><svg class="icon" viewBox="0 0 12 12" fill="none" stroke="#1b1b1b" stroke-width="1"><rect x="1" y="5" width="3" height="6"/><path d="M4 5l3-4c1 0 1.5.7 1.2 1.8L7.8 5H11v2l-1.5 4H4"/></svg>CHALLENGE</h4>
        <p>Poor solubility, instability, first-pass metabolism, and GI irritation often lead to low or inconsistent bioavailability.</p>
      </div>
      <div class="why-block">
        <h4><svg class="icon" viewBox="0 0 12 12" fill="none" stroke="#1b1b1b" stroke-width="1"><circle cx="6" cy="6" r="3"/><path d="M5 9v2h2V9M6 0.5v1.5M1 6h1.5M9.5 6H11M2.5 2.5l1 1M9.5 2.5l-1 1"/></svg>SOLUTION</h4>
        <p>Liposomal and solid-lipid delivery systems protect active ingredients, improve dissolution, and enhance absorption.</p>
      </div>
    </div>
    <p class="why-punch">Better delivery =<br>Better Clinical Outcomes</p>
  </section>

  <section class="slide col-a row-3">
    <div class="brand header-brand"><span class="brand-dot"></span><span class="brand-name">NUTRIVERA</span></div>
    <div class="header-rule"></div>
    <h2 class="header-title">WHAT IS A LIPOSOME?</h2>
    <div class="corner-dots" role="img" aria-label="Teal dot pattern"></div>
    <div class="lipo-figure" role="img" aria-label="Labelled cross-section illustration of a liposome structure"></div>
    <div class="lipo-rule"></div>
    <p class="lipo-text">Liposomes are microscopic spheres made of natural phospholipids that mimic human cell membranes, allowing nutrients to be absorbed more efficiently.</p>
  </section>

  <section class="slide col-b row-3">
    <div class="brand header-brand"><span class="brand-dot"></span><span class="brand-name">NUTRIVERA</span></div>
    <div class="header-rule"></div>
    <h2 class="header-title">STABILITY LEVERS IN DRIED LIPOSOMES</h2>
    <div class="corner-dots" role="img" aria-label="Teal dot pattern"></div>
    <ul class="bullets stab-list">
      <li>Matrix (carriers, glass transition)</li>
      <li>Residual moisture</li>
      <li>Antioxidants/chelators</li>
      <li>Particle size &amp; agglomeration</li>
      <li>Packaging &amp; water activity</li>
    </ul>
    <div class="stab-figure" role="img" aria-label="3D illustration of a liposome cross-section"></div>
  </section>

  <section class="slide col-a row-4">
    <div class="brand header-brand"><span class="brand-dot"></span><span class="brand-name">NUTRIVERA</span></div>
    <div class="header-rule"></div>
    <h2 class="header-title">MECHANISMS: WHY LIPOSOMAL POWDERS HELP</h2>
    <div class="corner-dots" role="img" aria-label="Teal dot pattern"></div>
    <div class="mech-photo" role="img" aria-label="3D render of colourful liposome particles"></div>
    <ul class="bullets mech-list">
      <li>Protect from GI degradation (acid/enzymes)</li>
      <li>Promote lymphatic/enterocyte uptake</li>
      <li>Faster dissolution of hydrophobic actives micro/nano-scale improves surface area</li>
      <li>Better dose uniformity vs liquids</li>
    </ul>
  </section>

  <section class="slide col-b row-4 closing">
    <div class="closing-dots" role="img" aria-label="Faint dot pattern"></div>
    <div class="brand closing-brand"><span class="brand-dot"></span><span class="brand-name">NUTRIVERA</span></div>
    <p class="closing-title">Thank You</p>
  </section>

</main>
</body>
</html>
```